Sales banner for E-commerce

This banner is intended for an e-commerce site selling motorcycle equipment and accessories.
The banner announces the sales and leads the customer to an offer of helmets, equipment, and accessories for motorcyclists.
The style of the banner must be modern, elegant, and both show that the prices are attractive and make you want to click to discover the offer of sale products behind it.
I insist on the aesthetics and the marketing side of the banner which are two absolutely essential elements.
Banner format 3840 (W) x 1250 (H)
Updates
Faible participation designers
Target Market(s)
Biker clientele in the general sense
Industry/Entity Type
Ecommerce Equipement et accessoires moto
Requirements
Must have
- Represent or inspire the motorcycle universe.
Nice to have
- The banner must be attractive and make you want to click

```html
<!DOCTYPE html>
<html lang="en">
<head>
<meta charset="utf-8">
<title>Motorcycle Equipment Sale Banner</title>
<link rel="stylesheet" href="https://fonts.googleapis.com/css2?family=Montserrat:wght@300;400;700;800&display=swap">
<style>
  :root {
    --ink-dark: #1c1c1e;
    --red-deep: #c4202c;
    --red-bright: #f2323c;
    --red-tag: #f2212f;
    --red-soft: #f45a63;
    --white: #ffffff;
  }
  * { margin: 0; padding: 0; box-sizing: border-box; }
  html, body { width: 1200px; height: 391px; overflow: hidden; }
  body { font-family: "Montserrat", Arial, sans-serif; background: var(--ink-dark); }
  .banner {
    position: relative;
    width: 1200px;
    height: 391px;
    overflow: hidden;
  }
  .backdrop {
    position: absolute;
    inset: 0;
    background:
      linear-gradient(180deg, rgba(255,255,255,0.06) 0%, rgba(0,0,0,0) 55%, rgba(0,0,0,0.18) 100%),
      linear-gradient(90deg, var(--ink-dark) 0%, #2a2326 30%, #7a2b33 48%, var(--red-deep) 62%, var(--red-bright) 80%, var(--red-soft) 100%);
  }
  .road-lines {
    position: absolute;
    inset: 0;
  }
  .gear-lineup {
    position: absolute;
    left: 600px;
    top: 48px;
    width: 500px;
    height: 310px;
    background:
      radial-gradient(ellipse 22% 38% at 18% 72%, rgba(235,235,238,0.85) 0%, rgba(235,235,238,0) 100%),
      radial-gradient(ellipse 12% 18% at 22% 30%, rgba(245,140,40,0.85) 0%, rgba(245,140,40,0) 100%),
      radial-gradient(ellipse 20% 40% at 88% 50%, rgba(205,205,210,0.9) 0%, rgba(205,205,210,0) 100%),
      radial-gradient(ellipse 30% 48% at 50% 48%, rgba(22,22,24,0.98) 0%, rgba(22,22,24,0.9) 55%, rgba(22,22,24,0) 100%),
      radial-gradient(ellipse 22% 26% at 56% 80%, rgba(30,30,38,0.95) 0%, rgba(30,30,38,0) 100%),
      radial-gradient(ellipse 14% 14% at 86% 84%, rgba(28,28,30,0.9) 0%, rgba(28,28,30,0) 100%);
  }
  .offer-tag {
    position: absolute;
    left: 84px;
    top: 106px;
    width: 326px;
    height: 66px;
    background: var(--red-tag);
    border-radius: 14px 46px 0 14px;
    display: flex;
    align-items: center;
    padding-left: 24px;
    color: var(--white);
    font-size: 39px;
    letter-spacing: 0.5px;
    line-height: 1;
  }
  .offer-tag .lead { font-weight: 300; margin-right: 11px; }
  .offer-tag .amount { font-weight: 800; }
  .headline {
    position: absolute;
    left: 95px;
    top: 182px;
    color: var(--white);
    font-weight: 700;
    font-size: 30px;
    line-height: 37px;
    letter-spacing: 0.2px;
    text-transform: uppercase;
  }
  .cta {
    position: absolute;
    left: 97px;
    top: 265px;
    width: 147px;
    height: 39px;
    border: 1.5px solid var(--white);
    border-radius: 20px;
    background: #111113;
    color: var(--white);
    font-weight: 700;
    font-size: 13px;
    letter-spacing: 0.3px;
    display: flex;
    align-items: center;
    justify-content: center;
    text-decoration: none;
  }
</style>
</head>
<body>
  <main class="banner">
    <div class="backdrop" role="img" aria-label="City skyline above a highway, fading from dark grey on the left to red on the right"></div>
    <svg class="road-lines" width="1200" height="391" viewBox="0 0 1200 391" aria-hidden="true">
      <line x1="160" y1="368" x2="625" y2="305" stroke="#ffffff" stroke-opacity="0.25" stroke-width="3"/>
      <line x1="1145" y1="235" x2="1200" y2="228" stroke="#ffffff" stroke-opacity="0.45" stroke-width="3"/>
      <line x1="1170" y1="287" x2="1200" y2="280" stroke="#ffffff" stroke-opacity="0.45" stroke-width="3"/>
      <line x1="790" y1="391" x2="1200" y2="325" stroke="#ffffff" stroke-opacity="0.35" stroke-width="3"/>
    </svg>
    <div class="gear-lineup" role="img" aria-label="Motorcycle gear lineup: white modular helmet, orange back protector, black textile riding jacket, matte black full-face helmet, light grey mesh jacket and black riding gloves"></div>
    <div class="offer-tag"><span class="lead">GET</span><span class="amount">25% OFF</span></div>
    <h1 class="headline">On motorcycle equipment<br>and accessories</h1>
    <a class="cta" href="#">SHOP NOW</a>
  </main>
</body>
</html>
```